Website Redesign

I am looking to have our website redone. We recently paid to have this done and are very unhappy with the results. We're looking to have a much more modern and clean feeling while GREATLY enhancing the user experience. We are very close to have a new logo designed as well as having some brand colors (Pantone 3005C). We want our site to have a human feel to it without focusing completely on our products. That being said, we need our products to play a more prominent role as our current site doesn't very clearly display what we do.
Our website: kvhomewares.com
Websites we like (overall feel): jogluma.com, oswaldtrent.com
Websites we like (functionality): birchvault.com
Updates
I apologize, we are new to ArtHivePro. I am showing a budget of $500 for this project. I know we'd go beyond that. I do not believe that we'll be able to overhaul our website for $500. I apologize for any confusion.

```html
<!DOCTYPE html>
<html lang="en">
<head>
<meta charset="utf-8">
<title>KV Homewares – Commercial Furniture</title>
<link href="https://fonts.googleapis.com/css2?family=Questrial&display=swap" rel="stylesheet">
<style>
  :root {
    --brand-blue: #0a80c6;
    --ink: #1c1c1c;
    --hero-black: #070707;
    --footer-grey: #e4e4e4;
    --footer-text: #333333;
    --white: #ffffff;
  }
  * { margin: 0; padding: 0; box-sizing: border-box; }
  html, body { width: 1200px; height: 830px; overflow: hidden; background: var(--white); }
  .page { position: relative; width: 1200px; height: 830px; font-family: "Questrial", sans-serif; color: var(--ink); }

  .top-rule { position: absolute; left: 0; top: 0; width: 100%; height: 9px; background: var(--brand-blue); }
  .brand-band { position: absolute; left: 0; top: 235px; width: 100%; height: 212px; background: var(--brand-blue); }

  .site-name { position: absolute; left: 132px; top: 78px; display: flex; align-items: center; gap: 10px;
    font-size: 34px; color: var(--ink); letter-spacing: 1px; }
  .site-name .dot { width: 12px; height: 12px; border-radius: 50%; background: var(--brand-blue); }

  .hero { position: absolute; left: 72px; top: 193px; width: 1056px; height: 292px; border-radius: 30px;
    background: var(--hero-black); border: 2px solid #000; overflow: hidden;
    box-shadow: 0 22px 26px -10px rgba(0,0,0,0.35); }
  .hero-photo { position: absolute; left: 0; top: 0; width: 460px; height: 100%;
    background: radial-gradient(ellipse at 38% 42%, #6b5a4a 0%, #3d4038 38%, #1b1f1b 70%, #070707 100%); }
  .hero-photo::after { content: ""; position: absolute; right: 0; top: 0; width: 120px; height: 100%;
    background: linear-gradient(90deg, rgba(7,7,7,0), var(--hero-black)); }
  .hero-art { position: absolute; left: 0; top: 0; }
  .hero-headline { position: absolute; left: 380px; top: 52px; color: var(--white); text-transform: uppercase; line-height: 1; }
  .hero-headline .small { display: block; font-size: 30px; letter-spacing: 1px; margin-bottom: 8px; }
  .hero-headline .large { display: block; font-size: 60px; letter-spacing: 1px; margin-bottom: 8px; }

  .intro { position: absolute; top: 538px; width: 430px; }
  .intro-welcome { left: 145px; }
  .intro-awesome { left: 646px; }
  .intro h2 { font-weight: 400; font-size: 29px; color: var(--brand-blue); text-align: center; margin-bottom: 14px;
    letter-spacing: 0.5px; }
  .intro p { font-size: 17px; line-height: 21.5px; letter-spacing: 1.6px; text-align: justify; width: 410px; }
  .intro .more { display: block; width: 428px; text-align: right; font-size: 21px; color: var(--brand-blue);
    text-decoration: underline; line-height: 14px; }

  .site-footer { position: absolute; left: 0; top: 766px; width: 100%; height: 64px;
    background: linear-gradient(180deg, #ececec, #dcdcdc); text-align: center;
    font-family: Arial, Helvetica, sans-serif; font-size: 15px; line-height: 18px; color: var(--footer-text); padding-top: 14px; }
</style>
</head>
<body>
<div class="page">
  <div class="top-rule"></div>
  <div class="brand-band"></div>

  <header class="site-name"><span>KV Homewares</span><span class="dot"></span></header>

  <section class="hero">
    <div class="hero-photo" role="img" aria-label="Portrait photograph of a woman wearing jewellery against a patterned backdrop"></div>
    <svg class="hero-art" width="1056" height="292" viewBox="0 0 1056 292" aria-hidden="false">
      <defs>
        <linearGradient id="glossPanel" x1="0" y1="0" x2="1" y2="1">
          <stop offset="0" stop-color="#6a6a6a"/>
          <stop offset="0.35" stop-color="#3a3a3a"/>
          <stop offset="1" stop-color="#141414"/>
        </linearGradient>
        <path id="arcCompany" d="M36,100 A64,64 0 0 1 100,36"/>
        <path id="arcProducts" d="M100,36 A64,64 0 0 1 164,100"/>
        <path id="arcOrdering" d="M36,100 A64,64 0 0 0 100,164"/>
        <path id="arcContact" d="M100,164 A64,64 0 0 0 164,100"/>
      </defs>
      <path d="M823,0 L1028,0 Q1056,0 1056,28 L1056,264 Q1056,292 1028,292 L872,292 C852,200 900,70 823,0 Z" fill="url(#glossPanel)"/>
      <g class="nav-wheel" transform="translate(788,46)" font-family="Questrial, sans-serif" font-size="13" letter-spacing="1">
        <circle cx="100" cy="100" r="92" fill="#2a2a2a"/>
        <path d="M11,97 A89,89 0 0 1 97,11 L97,60 A40,40 0 0 0 60,97 Z" fill="#1e1e1e" stroke="#555" stroke-width="1.5"/>
        <path d="M103,11 A89,89 0 0 1 189,97 L140,97 A40,40 0 0 0 103,60 Z" fill="#8d8d8d" stroke="#aaa" stroke-width="1.5"/>
        <path d="M11,103 A89,89 0 0 0 97,189 L97,140 A40,40 0 0 1 60,103 Z" fill="#2e2e2e" stroke="#555" stroke-width="1.5"/>
        <path d="M103,189 A89,89 0 0 0 189,103 L140,103 A40,40 0 0 1 103,140 Z" fill="#262626" stroke="#555" stroke-width="1.5"/>
        <circle cx="100" cy="100" r="36" fill="#000"/>
        <text fill="#ffffff"><textPath href="#arcCompany" startOffset="50%" text-anchor="middle">COMPANY</textPath></text>
        <text fill="#ffffff"><textPath href="#arcProducts" startOffset="50%" text-anchor="middle">PRODUCTS</textPath></text>
        <text fill="#ffffff"><textPath href="#arcOrdering" startOffset="50%" text-anchor="middle" dy="10">ORDERING</textPath></text>
        <text fill="#ffffff"><textPath href="#arcContact" startOffset="50%" text-anchor="middle" dy="10">CONTACT</textPath></text>
        <path d="M14,44 L34,30 L30,54 Z" fill="#e8741c"/>
      </g>
    </svg>
    <h1 class="hero-headline">
      <span class="small">We make comercial</span>
      <span class="large">Furniture</span>
      <span class="small">That’s inherently</span>
      <span class="large">Human</span>
    </h1>
  </section>

  <section class="intro intro-welcome">
    <h2>WELCOME TO KV HOMEWARES</h2>
    <p>Lorem ipsum dolor sit amet, consectetur adipisicing elit, sed do eiusmod tempor incididunt ut labore et dolore magna aliqua. Ut enim ad minim veniam, quis nostrud exercitation ullamco laboris nisi ut aliquip ex</p>
    <a class="more" href="#">more</a>
  </section>

  <section class="intro intro-awesome">
    <h2>WHAT MAKE US AWESOME?</h2>
    <p>Lorem ipsum dolor sit amet, consectetur adipisicing elit, sed do eiusmod tempor incididunt ut labore et dolore magna aliqua. Ut enim ad minim veniam, quis nostrud exercitation ullamco laboris nisi ut aliquip ex</p>
    <a class="more" href="#">more</a>
  </section>

  <footer class="site-footer">
    © 2013 KV Homewares | 418 Linden Harbor Road, Suite 210, Fairbrook, WI 53990<br>
    Call Toll-free: 800.555.0148 | Fax: 859.555.0172 | Email Us
  </footer>
</div>
</body>
</html>
```